creating a certificate for our flagship course

Hi,
We need a new certificate for our flagship course called Rising Tide. We have been running this course for 25 years this year and want to get something special that represents that. We need our logos incorporated and we love to have a compass or Koru incorporated in the certificate. We like something different from your standard certificate, but not too crazy.

The text should say something along the lines of:
This certificate is awarded to ....
For successfully completing and contributing to the three day Rising Tide programme.

signed:... date:...

to learn a bit more about this course and our company, please check our website. www.veldonmarstik.co.nz

Thank you!

attendees who completed our 3 day programme.

• Both our RT logo and our brand logo. a compass or a koru.
• a 25th year existence something on it.

```html
<!DOCTYPE html>
<html lang="en">
<head>
<meta charset="utf-8">
<title>Rising Tide Programme Certificate</title>
<link rel="stylesheet" href="https://fonts.googleapis.com/css2?family=Cinzel:wght@400;600;700&family=Pinyon+Script&display=swap">
<style>
  :root {
    --navy: #23264f;
    --paper: #ffffff;
    --paper-shade: #eef0f3;
    --ink: #23264f;
    --muted: #5a5d78;
    --band-text: #ffffff;
    --accent-green: #8cc63f;
  }
  * { margin: 0; padding: 0; box-sizing: border-box; }
  html, body { width: 900px; height: 1200px; overflow: hidden; }
  body { background: var(--paper-shade); }
  .certificate {
    position: relative;
    width: 900px;
    height: 1200px;
    background: linear-gradient(135deg, var(--paper) 0%, #f7f8fa 60%, var(--paper-shade) 100%);
    color: var(--ink);
    font-family: "Cinzel", serif;
    text-align: center;
  }
  .top-band {
    position: absolute;
    left: 323px;
    top: 0;
    width: 212px;
    height: 384px;
    background: var(--navy);
    border-radius: 0 0 106px 106px;
  }
  .brand {
    position: absolute;
    left: 0; right: 0;
    top: 60px;
    display: flex;
    flex-direction: column;
    align-items: center;
    color: var(--band-text);
  }
  .brand-mark {
    width: 64px; height: 64px;
    background: var(--band-text);
    margin-bottom: 18px;
  }
  .brand-name {
    font-size: 19px;
    font-weight: 400;
    letter-spacing: 1px;
    line-height: 1.2;
  }
  .programme {
    position: absolute;
    left: 0; right: 0;
    top: 240px;
    display: flex;
    align-items: center;
    justify-content: center;
    gap: 10px;
    color: var(--band-text);
  }
  .programme-mark {
    width: 56px; height: 56px;
    border-radius: 50%;
    background: var(--accent-green);
  }
  .programme-name {
    font-size: 17px;
    font-weight: 400;
  }
  .band-swoosh {
    position: absolute;
    left: 0; top: 0;
    width: 900px; height: 460px;
  }
  .title {
    position: absolute;
    left: 0; right: 0;
    top: 365px;
    font-family: "Pinyon Script", cursive;
    font-size: 150px;
    line-height: 1;
    color: var(--ink);
  }
  .awarded {
    position: absolute;
    left: 0; right: 0;
    top: 598px;
    font-size: 31px;
    font-weight: 600;
    letter-spacing: 1px;
  }
  .recipient {
    position: absolute;
    left: 0; right: 0;
    top: 655px;
    font-family: "Pinyon Script", cursive;
    font-size: 80px;
    line-height: 1;
  }
  .recipient-line {
    position: absolute;
    left: 240px;
    top: 748px;
    width: 420px;
    height: 1px;
    background: var(--muted);
  }
  .citation {
    position: absolute;
    left: 0; right: 0;
    top: 815px;
    font-size: 35px;
    font-weight: 700;
    line-height: 51px;
    letter-spacing: 1.5px;
  }
  .divider {
    position: absolute;
    left: 220px;
    top: 1040px;
    width: 460px;
    height: 3px;
    background: linear-gradient(90deg, transparent, var(--muted) 30%, var(--muted) 70%, transparent);
  }
  .place-date, .signatory {
    position: absolute;
    top: 1125px;
    font-family: "Cinzel", serif;
    font-size: 15px;
    font-weight: 400;
    color: var(--muted);
    text-align: left;
    line-height: 1.4;
    text-transform: none;
  }
  .place-date { left: 55px; }
  .signatory { left: 730px; }
  .anniversary-tab {
    position: absolute;
    left: 323px;
    top: 1070px;
    width: 212px;
    height: 130px;
    background: var(--navy);
    border-radius: 106px 106px 0 0;
    color: var(--band-text);
  }
  .anniversary-number {
    display: block;
    margin-top: 28px;
    font-family: "Cinzel", serif;
    font-size: 60px;
    font-weight: 700;
    line-height: 1;
  }
  .anniversary-label {
    display: block;
    font-family: "Pinyon Script", cursive;
    font-size: 30px;
    line-height: 1;
    margin-top: -4px;
  }
</style>
</head>
<body>
  <main class="certificate">
    <svg class="band-swoosh" viewBox="0 0 900 460" aria-hidden="true">
      <path d="M300 300 Q330 420 430 410 Q520 402 560 320" fill="none" stroke="#9a9cb3" stroke-width="2"/>
      <path d="M560 320 Q600 230 620 180" fill="none" stroke="#c4c6d4" stroke-width="1.5"/>
    </svg>
    <div class="top-band">
      <div class="brand">
        <span class="brand-mark"></span>
        <span class="brand-name">VELDON<br>MARSTIK<br>&amp; Associates</span>
      </div>
      <div class="programme">
        <span class="programme-mark"></span>
        <span class="programme-name">Rising Tide</span>
      </div>
    </div>

    <h1 class="title">Certificate</h1>
    <p class="awarded">THIS CERTIFICATE IS AWARDED TO</p>
    <p class="recipient">Daniel Hartley</p>
    <span class="recipient-line"></span>
    <p class="citation">FOR SUCCESSFULLY COMPLETING<br>AND CONTRIBUTING TO THE<br>THREE DAY RISING TIDE<br>PROGRAMME</p>

    <span class="divider"></span>
    <p class="place-date">Dunedin,<br>30.4.2016.</p>
    <p class="signatory">Chairman</p>

    <div class="anniversary-tab">
      <span class="anniversary-number">25</span>
      <span class="anniversary-label">years</span>
    </div>
  </main>
</body>
</html>
```